Building Custom Homes

We need a new business card design for a new company called " T & R Custom Homes" . We built custom homes according to our client's dream home. We would like to see designs that use the color blue, green, yellow, orange, pink depicting a home happy 'n bright!

Industry/Entity Type

Business

Contact Information for Business Card

Email: porvinta73@kelbrix.com.au Mobile: 0427 318 946 Phone: 02 6781 4053 Address: Shop 3 / 72 Wexbury Street Lorindale, NSW 2461 Builders License Number : 47 08 3K ABN : 63 519 874 027 Name: Owen Bask

Colors
0355a3
0392cd
9bcb3c
e34297
f78f20
fbed22

Requirements
Must have
• The Company Name : "T & R Custom Homes"
• must depict the building industry

```html
<!DOCTYPE html>
<html lang="en">
<head>
<meta charset="utf-8">
<title>T &amp; R Custom Homes – Business Card</title>
<link rel="stylesheet" href="https://fonts.googleapis.com/css2?family=Questrial&display=swap">
<style>
  :root {
    --backdrop: #dcdcde;
    --card: #ffffff;
    --card-edge: #9a9a9a;
    --ink: #2e2e2e;
    --ink-soft: #444444;
    --brand-blue: #0392cd;
    --brand-orange: #f78f20;
  }
  * { margin: 0; padding: 0; box-sizing: border-box; }
  html, body {
    width: 1164px;
    height: 1200px;
    overflow: hidden;
    background: var(--backdrop);
    font-family: "Questrial", "Century Gothic", sans-serif;
    color: var(--ink);
  }
  .card {
    position: absolute;
    left: 82px;
    top: 265px;
    width: 1000px;
    height: 670px;
    background: var(--card);
    border: 2px solid var(--card-edge);
    overflow: hidden;
  }
  .company-name {
    position: absolute;
    top: 78px;
    left: 0;
    width: 100%;
    text-align: center;
    font-size: 58px;
    font-weight: 400;
    letter-spacing: 0.5px;
    color: var(--ink);
    -webkit-text-stroke: 0.6px var(--ink);
  }
  .tagline {
    position: absolute;
    top: 166px;
    left: 0;
    width: 100%;
    text-align: center;
    font-size: 16px;
    color: var(--ink-soft);
  }
  .name-tab {
    position: absolute;
    left: 0;
    top: 221px;
    width: 23px;
    height: 152px;
    background: var(--brand-blue);
    border-radius: 0 8px 8px 0;
  }
  .person-name {
    position: absolute;
    left: 46px;
    top: 262px;
    font-size: 58px;
    font-weight: 400;
    color: var(--ink);
    -webkit-text-stroke: 0.6px var(--ink);
  }
  .contact {
    position: absolute;
    left: 412px;
    top: 372px;
    font-size: 25px;
    line-height: 32px;
    color: var(--ink-soft);
  }
  .contact-row {
    display: flex;
    align-items: flex-start;
    gap: 14px;
  }
  .contact-row + .contact-row { margin-top: 14px; }
  .contact-row.email { margin-top: 6px; gap: 8px; }
  .contact-icon {
    flex: 0 0 26px;
    width: 26px;
    height: 26px;
    margin-top: 3px;
    fill: var(--ink);
  }
  .contact-row.email .contact-icon { flex-basis: 20px; width: 20px; margin-top: 6px; }
  .accent-bands {
    position: absolute;
    left: 0;
    bottom: 8px;
    width: 100%;
    height: 20px;
  }
  .band { position: absolute; top: 0; height: 100%; }
  .band-left { left: 0; width: 321px; background: var(--brand-blue); }
  .band-middle { left: 332px; width: 324px; background: var(--brand-orange); }
  .band-right { left: 670px; right: 0; background: var(--brand-blue); }
</style>
</head>
<body>
  <article class="card">
    <h1 class="company-name">T &amp; R Custom Homes</h1>
    <p class="tagline">The Bright Homebuilder Promise</p>

    <div class="name-tab"></div>
    <h2 class="person-name">Owen Bask</h2>

    <div class="contact">
      <div class="contact-row address">
        <svg class="contact-icon" viewBox="0 0 24 24" aria-hidden="true">
          <path d="M12 3 2 12h3v9h5v-6h4v6h5v-9h3z"/>
        </svg>
        <p>Address: Shop 3 / 72 Wexbury Street<br>Lorindale, NSW 2461 Builders License<br>Number : 47 08 3K ABN : 63 519 874 027</p>
      </div>
      <div class="contact-row phone">
        <svg class="contact-icon" viewBox="0 0 24 24" aria-hidden="true">
          <path d="M6.6 10.8a15 15 0 0 0 6.6 6.6l2.2-2.2a1 1 0 0 1 1-.25 11.4 11.4 0 0 0 3.6.57 1 1 0 0 1 1 1V20a1 1 0 0 1-1 1A17 17 0 0 1 3 4a1 1 0 0 1 1-1h3.5a1 1 0 0 1 1 1c0 1.25.2 2.45.57 3.6a1 1 0 0 1-.25 1z"/>
        </svg>
        <p>0427 318 946<br>02 6781 4053</p>
      </div>
      <div class="contact-row email">
        <svg class="contact-icon" viewBox="0 0 24 18" aria-hidden="true">
          <path d="M1 1h22v16H1zm2 2v.6l9 6 9-6V3zm0 3v9h18V6l-9 6z"/>
        </svg>
        <p>porvinta73@kelbrix.com.au</p>
      </div>
    </div>

    <div class="accent-bands">
      <span class="band band-left"></span>
      <span class="band band-middle"></span>
      <span class="band band-right"></span>
    </div>
  </article>
</body>
</html>
```